Veranaxis Business Card and Letter Head

We are a leadership assessment consultancy based in Sydney, Australia. We help executive-level decison-makers select leaders for more senior level roles in corporate and government organisations. Our methodology is based on the latest research from the field of neuroscience.
We need a business card design and matching letter head that presents our company, Veranaxis, as a:
1. trusted adviser to senior executive-level decison makers
2. niche consultancy who are experts in the field of assessing leadership talent
3. results-focused solution provider who balance scientific methods with pragmatic solutions
The following company details should be used in all designs:
Company Name: Veranaxis
Details (for business card):
Daniel Prescott
High Potential Officer
Level 29, Brenning Tower
7 Brenning Square
Sydney, NSW 2000 Australia
Phone: 1300 482 716
Mobile: 0412 573 208
Email: daniel.prescott@veranaxis.com.au
Website: veranaxis.com.au
I have attached the logo for Veranaxis (for both a white and black background) - your business card and letter head designs must incoporate this logo and colour scheme.
Thanks for your interest in this project, I'm looking forward to receiving your ideas.
Regards,
Daniel
Executive-level decison-makers in corporate and government organisations (e.g., CEO, VP, Head of Human Resources)
Leadership

```html
<!DOCTYPE html>
<html lang="en">
<head>
<meta charset="utf-8">
<title>Veranaxis Letterhead</title>
<link rel="stylesheet" href="https://fonts.googleapis.com/css2?family=Roboto+Condensed:wght@400;700&display=swap">
<style>
  :root {
    --paper: #ffffff;
    --ink: #2b2b2b;
    --rule: #3a3a3a;
    --accent: #c8321e;
  }
  html, body {
    margin: 0;
    padding: 0;
    overflow: hidden;
    background: var(--paper);
  }
  .letterhead {
    position: relative;
    width: 870px;
    height: 1200px;
    background: var(--paper);
    font-family: "Roboto Condensed", "Arial Narrow", sans-serif;
    color: var(--ink);
    overflow: hidden;
  }
  .side-rule {
    position: absolute;
    left: 829px;
    top: 0;
    width: 9px;
    height: 672px;
    background: var(--rule);
  }
  .brand-name {
    position: absolute;
    left: 782px;
    top: 957px;
    transform-origin: 0 0;
    transform: rotate(-90deg);
    margin: 0;
    font-weight: 700;
    font-size: 56px;
    line-height: 56px;
    color: var(--ink);
    letter-spacing: -0.5px;
    white-space: nowrap;
  }
  .brand-square {
    position: absolute;
    left: 800px;
    top: 1040px;
    width: 32px;
    height: 32px;
    background: var(--accent);
  }
  .corner-bracket {
    position: absolute;
    left: 44px;
    top: 1032px;
    width: 56px;
    height: 56px;
  }
  .corner-bracket polygon { fill: var(--rule); }
  .contact {
    position: absolute;
    top: 1050px;
    margin: 0;
    font-style: normal;
    font-weight: 400;
    font-size: 10.5px;
    line-height: 14px;
    letter-spacing: -0.1px;
  }
  .contact p { margin: 0; }
  .contact-address { left: 116px; }
  .contact-lines { left: 298px; }
</style>
</head>
<body>
  <main class="letterhead">
    <div class="side-rule"></div>

    <p class="brand-name">Veranaxis</p>
    <span class="brand-square"></span>

    <svg class="corner-bracket" viewBox="0 0 56 56" aria-hidden="true">
      <polygon points="0,0 56,0 56,14 14,14 14,56 0,56"/>
    </svg>

    <address class="contact contact-address">
      <p>Level 29, Brenning Tower</p>
      <p>7 Brenning Square</p>
      <p>Sydney, NSW 2000 Australia</p>
    </address>

    <div class="contact contact-lines">
      <p>Phone: 1300 482 716</p>
      <p>Mobile: 0412 573 208</p>
      <p>Email: daniel.prescott@veranaxis.com.au</p>
      <p>Website: veranaxis.com.au</p>
    </div>
  </main>
</body>
</html>
```